Gestaltung von Bilder/Icons mit den wichtigsten Fakten des Unternehmens aus 15 Jahren
Zielgruppe
Vireto Verkauft online und in Galerien Fotokunst auf höchstem Niveau. Alle Infos findet man auch online unter: https://www.vireto.de/unsere-editionen/#prinzip
Zu unserem 15-Jährigen Firmenjubiläum möchten wir eine ansprechende Infografik auf unserer Website und in den Galerien zeigen. Hier: https://www.vireto.de/15-jahre-vireto/
Beispiele sind diesem Briefing beigefügt.
Aufgabenstellung
Die Infografik soll bitte folgende Informationen verarbeiten:
536 Editionen von Künstlern verlegt
Künstlerische Freiheit mit 21.650.350 € an Honoraren gefördert
Ermöglicht durch 134 VIRETO-Mitarbeiter
28 Galerien weltweit
246.912 zufriedene Kunden
687.601 signierte, limitierte Editionen ausgeliefert
Kunstsammler in 129 Ländern beliefert
1.612 Vernissagen, Events und Lesungen
532.567 Besucher pro Jahr

```html
<!DOCTYPE html>
<html lang="de">
<head>
<meta charset="utf-8">
<title>15 Jahre Vireto – Fakten</title>
<link rel="stylesheet" href="https://fonts.googleapis.com/css2?family=Barlow+Condensed:wght@600&family=Barlow+Semi+Condensed:wght@400;700&display=swap">
<style>
  :root {
    --wall: #2d2d2d;
    --frame: #1a1a1a;
    --mat: #ffffff;
    --ink: #141414;
    --accent: #29abe2;
  }
  * { margin: 0; padding: 0; box-sizing: border-box; }
  html, body { width: 1200px; height: 848px; overflow: hidden; background: var(--wall); }
  .wall { position: relative; width: 1200px; height: 848px; }
  .frame { position: absolute; background: var(--frame); padding: 27px; }
  .mat { position: relative; width: 100%; height: 100%; background: var(--mat); color: var(--ink); }
  .mat > * { position: absolute; }
  .figure {
    font-family: "Barlow Condensed", sans-serif;
    font-weight: 600;
    font-size: 60px;
    line-height: 1;
    letter-spacing: -0.5px;
  }
  .label {
    font-family: "Barlow Semi Condensed", sans-serif;
    font-weight: 400;
    font-size: 15px;
    line-height: 17px;
    text-transform: uppercase;
    white-space: nowrap;
  }
  .label b { font-weight: 700; }
  .icon { fill: var(--accent); }
  .center { left: 0; right: 0; text-align: center; }
</style>
</head>
<body>
<main class="wall">

  <!-- Editionen -->
  <section class="frame" style="left:316px;top:38px;width:229px;height:209px">
    <div class="mat">
      <p class="figure" style="left:26px;top:20px">536</p>
      <svg class="icon" style="left:114px;top:12px" width="46" height="74" viewBox="0 0 46 74" aria-hidden="true">
        <path d="M34 2 l10 6 -4 7 -10 -6z"/>
        <path d="M28 12 l10 6 -26 46 -10 -6z"/>
        <path d="M1 60 l10 6 -12 8z"/>
      </svg>
      <p class="label" style="left:26px;top:88px"><b>Editionen</b><br>von <b>Künstlern</b><br>verlegt</p>
    </div>
  </section>

  <!-- Kunden -->
  <section class="frame" style="left:577px;top:66px;width:318px;height:181px">
    <div class="mat">
      <svg class="icon" style="left:23px;top:30px" width="42" height="38" viewBox="0 0 42 38" aria-hidden="true">
        <path d="M21 38 C8 28 0 20 0 11 0 4 5 0 11 0 16 0 19 3 21 6 23 3 26 0 31 0 37 0 42 4 42 11 42 20 34 28 21 38z"/>
      </svg>
      <p class="figure" style="left:78px;top:22px">246.912</p>
      <p class="label" style="left:79px;top:84px"><b>Zufriedene</b> Kunden</p>
    </div>
  </section>

  <!-- Events -->
  <section class="frame" style="left:46px;top:234px;width:238px;height:283px">
    <div class="mat">
      <svg class="icon" style="left:63px;top:32px" width="58" height="55" viewBox="0 0 58 55" aria-hidden="true">
        <path d="M29 0 L36 20 58 21 41 34 47 55 29 43 11 55 17 34 0 21 22 20z"/>
      </svg>
      <p class="figure center" style="top:100px">1.612</p>
      <p class="label center" style="top:167px">Vernissagen, Events<br>und Lesungen</p>
    </div>
  </section>

  <!-- Honorare -->
  <section class="frame" style="left:316px;top:280px;width:358px;height:238px">
    <div class="mat">
      <p class="label" style="left:28px;top:47px"><b>Künstlerische</b><br><b>Freiheit</b> mit</p>
      <div role="img" aria-label="Fliegender Vogel als Symbol der künstlerischen Freiheit" style="left:143px;top:14px;width:78px;height:64px;background:var(--accent);border-radius:60% 40% 50% 50%"></div>
      <p class="figure" style="left:27px;top:88px">21.650.350 €</p>
      <p class="label" style="left:28px;top:150px">an <b>Honoraren</b> gefördert</p>
    </div>
  </section>

  <!-- Galerien -->
  <section class="frame" style="left:705px;top:280px;width:190px;height:238px">
    <div class="mat">
      <p class="figure" style="left:19px;top:52px">28</p>
      <svg class="icon" style="left:73px;top:23px" width="38" height="53" viewBox="0 0 38 53" aria-hidden="true">
        <path d="M19 0 C8.5 0 0 8.5 0 19 0 31 19 53 19 53 S38 31 38 19 C38 8.5 29.5 0 19 0z"/>
        <path d="M12 13 h14 v14 h-3 v-11 h-11z" fill="#fff"/>
      </svg>
      <p class="label" style="left:19px;top:114px"><b>Galerien</b><br><b>weltweit</b></p>
    </div>
  </section>

  <!-- Mitarbeiter -->
  <section class="frame" style="left:927px;top:313px;width:229px;height:205px">
    <div class="mat">
      <p class="label" style="left:27px;top:17px">Ermölicht durch</p>
      <svg class="icon" style="left:30px;top:49px" width="38" height="38" viewBox="0 0 38 38" aria-hidden="true">
        <circle cx="19" cy="9" r="9"/>
        <path d="M0 38 C0 26 6 20 12 19 Q19 24 26 19 C32 20 38 26 38 38z"/>
      </svg>
      <p class="figure" style="left:80px;top:40px">134</p>
      <p class="label" style="left:27px;top:102px"><b>Vireto-</b><br><b>Mitarbeiter</b></p>
    </div>
  </section>

  <!-- Länder -->
  <section class="frame" style="left:142px;top:549px;width:228px;height:262px">
    <div class="mat">
      <svg style="left:55px;top:28px" width="60" height="60" viewBox="0 0 60 60" aria-hidden="true">
        <circle cx="30" cy="30" r="30" fill="var(--accent)"/>
        <g fill="none" stroke="#fff" stroke-width="3">
          <ellipse cx="30" cy="30" rx="13" ry="30"/>
          <line x1="30" y1="0" x2="30" y2="60"/>
          <line x1="0" y1="30" x2="60" y2="30"/>
          <path d="M6 14 Q30 22 54 14"/>
          <path d="M6 46 Q30 38 54 46"/>
        </g>
      </svg>
      <p class="label" style="left:19px;top:102px">Kunstsammler in</p>
      <p class="figure" style="left:18px;top:126px">129</p>
      <p class="label" style="left:91px;top:145px"><b>Ländern</b><br>beliefert</p>
    </div>
  </section>

  <!-- Besucher -->
  <section class="frame" style="left:401px;top:547px;width:316px;height:164px">
    <div class="mat">
      <svg class="icon" style="left:21px;top:21px" width="37" height="62" viewBox="0 0 37 62" aria-hidden="true">
        <path d="M0 6 L26 0 V62 L0 56z"/>
        <path d="M28 4 H37 V58 H28 V55 H34 V7 H28z"/>
        <circle cx="17" cy="29" r="2.5" fill="#fff"/>
      </svg>
      <p class="figure" style="left:82px;top:18px">532.567</p>
      <p class="label" style="left:83px;top:81px"><b>Besucher</b> pro Jahr</p>
    </div>
  </section>

  <!-- Auslieferung -->
  <section class="frame" style="left:748px;top:547px;width:348px;height:216px">
    <div class="mat">
      <p class="figure" style="left:19px;top:20px">687.601</p>
      <p class="label" style="left:20px;top:83px">Signierte, limitierte<br><b>Editionen ausgeliefert</b></p>
      <svg style="left:185px;top:54px" width="88" height="90" viewBox="0 0 88 90" aria-hidden="true">
        <path d="M2 6 Q6 0 11 4 L32 76 L86 60" fill="none" stroke="var(--accent)" stroke-width="4" stroke-linecap="round"/>
        <circle cx="30" cy="80" r="7" fill="#fff" stroke="var(--accent)" stroke-width="4"/>
        <path d="M28 18 L71 7 L82 53 L39 64z" fill="var(--accent)"/>
        <path d="M50 48 L47 32 L42 34 L51 22 L58 30 L53 31 L56 46z" fill="#fff"/>
      </svg>
    </div>
  </section>

</main>
</body>
</html>
```